Online Digital Solutions Agency needs a New Business Card

We are a Online/Digital solution agency. We provide WordPress Solutions, Online & Digital Marketing Solutions including SEO, Social Media Marketing and Managed Hosting including VPS and Cloud Hosting solutions. We also design and build bespoke web sites and web applications for various clients. We are very good at site migrations, 3rd party API integrations and mobile app development.

We are rebranding our agency and have already designed a new logo. We have selected 5-6 colours as our base colour and are currently building our new website based around these colour scheme.

Our logo indicates that we are a cloud solution providers, and (i.e. the Clouds), and developers (i.e. HTML Tags, and CSS formats). We use the 5-6 base colours and use various shades of these colours as required.

Our old website is located at: www.brambleforgelabs.com

And our new website is going to be at (we are working on it at the moment ...):
https://creative.brambleforgelabs.co.uk/

Our slogan is "Digital Transformation Specialist"

What we mean by that is; we can take any existing business and get them up and transform them in to the digital world, starting with Hosting, Web Design, Development & Online Marketing aspects.

The powerpoint is a document that we use to present our projects to clients at the moment, and the cloud is on the background as we clarified earlier. (Just to get the idea)

What we are looking for is a Great WoW factor design to start with, ideally with the Logo and Logo colour scheme if possible but not required as long as the designers can do better, and basically give life to our logo and company via the Business card design.

Ideally with some icons perhaps to indicate the address, location, mobile, email, and website would be good but again optional as long as there is a good design.

The cloud can be used as a background if required in a light shade or as a watermark share perhaps.

The logos' and the Illustrator files are shared with you so you can use them as required.

Ideally the business card should have a Name, title, Mobile, Email , Website, Address and perhaps some social media links.

Target Market(s)

New Startups, SME's, Contract and Outsource Clients

Contact Information for Business Card

Company Name:
==============
BrambleForge Labs (UK) Ltd.

Tag Line:
========
“Digital Transformation Specialists”

Adress:
=======

Suite KR73054
14-16 Ashgrove Lane
London
E9 4PD.

Name:
=====
Idris Malek

Title: (Optional)
=============
FQTA, PgD (RNOM)

Role:
=====
Digital Solutions Architect

Email:
=====
idris@brambleforgelabs.uk

WebSite:
=======
http://www.brambleforgelabs.uk

OR

www.brambleforgelabs.uk

Mobile:
======
0044 (0)75 218 30479

OR

+44 (0)75 218 30479

LinkedIN: (Optional)
========
https://uk.linkedin.com/in/idrismalek

Skype: (Optional)
======
idris.malek

Twitter (Optional) : idrismalek

Font styles to use
Serif
Sans Serif

Requirements
Must have
• The Logo
• Business Name
• Person Name
• Title
• Mobile
• Email
• Website
• Address
• I have provided the colour scheme on my files.
Nice to have
• Twiter
• Linked in
• Facebook

```html
<!DOCTYPE html>
<html lang="en">
<head>
<meta charset="utf-8">
<title>BrambleForge Labs — Business Card</title>
<link rel="stylesheet" href="https://fonts.googleapis.com/css2?family=Raleway:wght@500;600;700&family=Roboto:wght@400&display=swap">
<style>
  :root {
    --page-bg: #e4e2dc;
    --card-bg: #fbfbfd;
    --brand-blue: #1c5ea8;
    --brand-mid: #2a8ad0;
    --brand-teal: #1ab0cf;
    --ink: #3f3f44;
    --ink-soft: #4c4c52;
  }
  * { margin: 0; padding: 0; box-sizing: border-box; }
  html, body { width: 1200px; height: 1200px; overflow: hidden; }
  body {
    background: var(--page-bg);
    position: relative;
    font-family: "Roboto", Arial, sans-serif;
  }
  .card {
    position: absolute;
    left: 207px;
    width: 786px;
    height: 448px;
    background: var(--card-bg);
    box-shadow: 0 1px 3px rgba(0,0,0,0.12);
  }
  .card-front { top: 125px; }
  .card-back { top: 628px; }

  .accent-bar {
    position: absolute; left: 0; top: 64px;
    width: 15px; height: 56px;
    background: var(--brand-blue);
  }
  .person-name {
    position: absolute; left: 46px; top: 58px;
    font-family: "Raleway", Arial, sans-serif;
    font-weight: 700; font-size: 36px;
    color: var(--brand-blue); line-height: 1;
  }
  .person-credentials {
    position: absolute; left: 46px; top: 105px;
    font-family: "Raleway", Arial, sans-serif;
    font-weight: 500; font-size: 17px;
    color: var(--ink); line-height: 1;
  }
  .person-role {
    position: absolute; left: 46px; top: 167px;
    font-family: "Raleway", Arial, sans-serif;
    font-weight: 600; font-size: 20px;
    color: var(--brand-teal); line-height: 1;
  }
  .address {
    position: absolute; left: 46px; top: 259px;
    font-weight: 400; font-size: 20px; line-height: 25px;
    color: var(--ink-soft);
  }
  .contact-list {
    position: absolute; list-style: none;
    font-weight: 400; font-size: 20px; color: var(--ink-soft);
  }
  .contact-list li {
    display: flex; align-items: center;
    height: 30px; gap: 8px;
  }
  .contact-main { left: 44px; top: 321px; }
  .contact-social { left: 450px; top: 355px; }
  .contact-icon { width: 22px; height: 22px; flex: none; }

  .brand-mark {
    position: absolute;
    display: flex; align-items: center;
    font-family: "Raleway", Arial, sans-serif;
    font-weight: 700; color: var(--brand-blue);
    white-space: nowrap;
  }
  .brand-dot { border-radius: 50%; background: var(--brand-mid); flex: none; }
  .brand-front { right: 48px; top: 104px; font-size: 31px; gap: 12px; }
  .brand-front .brand-dot { width: 26px; height: 26px; }
  .brand-back { left: 0; right: 0; justify-content: center; top: 168px; font-size: 52px; gap: 18px; }
  .brand-back .brand-dot { width: 44px; height: 44px; }

  .company-name {
    position: absolute; left: 0; right: 0; top: 344px;
    text-align: center; font-size: 20px; font-weight: 400; color: var(--brand-blue);
  }
  .company-address {
    position: absolute; left: 0; right: 0; top: 369px;
    text-align: center; font-size: 21px; font-weight: 400; color: var(--brand-mid);
  }
</style>
</head>
<body>

<section class="card card-front">
  <div class="accent-bar"></div>
  <h1 class="person-name">Idris Malek</h1>
  <p class="person-credentials">FQTA, PgD(RNOM)</p>
  <p class="person-role">Digital Solutions Architect</p>

  <div class="brand-mark brand-front"><span class="brand-dot"></span>BrambleForge Labs</div>

  <p class="address">14-16, Ashgrove Lane London<br>E9 4PD United Kingdom</p>

  <ul class="contact-list contact-main">
    <li>
      <svg class="contact-icon" viewBox="0 0 22 22" aria-hidden="true">
        <circle cx="11" cy="11" r="9.8" fill="none" stroke="var(--brand-blue)" stroke-width="1.4"/>
        <rect x="7.5" y="5" width="7" height="12" rx="1.3" fill="none" stroke="var(--brand-blue)" stroke-width="1.4"/>
        <line x1="10" y1="15" x2="12" y2="15" stroke="var(--brand-blue)" stroke-width="1.2"/>
      </svg>
      +44 (0)75 218 30479
    </li>
    <li>
      <svg class="contact-icon" viewBox="0 0 22 22" aria-hidden="true">
        <circle cx="11" cy="11" r="9.8" fill="none" stroke="var(--brand-blue)" stroke-width="1.4"/>
        <rect x="6" y="7.5" width="10" height="7" fill="var(--brand-blue)"/>
        <polyline points="6,7.5 11,11.5 16,7.5" fill="none" stroke="#fff" stroke-width="1"/>
      </svg>
      idris@brambleforgelabs.uk
    </li>
    <li>
      <svg class="contact-icon" viewBox="0 0 22 22" aria-hidden="true">
        <circle cx="11" cy="11" r="9.8" fill="none" stroke="var(--brand-blue)" stroke-width="1.4"/>
        <circle cx="11" cy="11" r="5.5" fill="var(--brand-blue)"/>
        <path d="M8 9 Q10 8 11 10 Q10 12 12 13 L11 15.5" fill="none" stroke="#fff" stroke-width="1"/>
      </svg>
      www.brambleforgelabs.uk
    </li>
  </ul>

  <ul class="contact-list contact-social">
    <li>
      <svg class="contact-icon" viewBox="0 0 22 22" aria-hidden="true"><circle cx="11" cy="11" r="10" fill="var(--brand-teal)"/></svg>
      idris.malek
    </li>
    <li>
      <svg class="contact-icon" viewBox="0 0 22 22" aria-hidden="true"><circle cx="11" cy="11" r="10" fill="var(--brand-blue)"/></svg>
      uk.proflink.net/in/idrismalek
    </li>
  </ul>
</section>

<section class="card card-back">
  <div class="brand-mark brand-back"><span class="brand-dot"></span>BrambleForge Labs</div>
  <p class="company-name">BRAMBLEFORGE LABS (UK) LIMITED.</p>
  <p class="company-address">14-16 Ashgrove Lane, London, E9 4PD, England, United Kingdom</p>
</section>

</body>
</html>
```